Hey, we loved your business cards ... now we require a A6 postcard please that fits our brand and communicates our new and exciting "Happy Hour" offer. The offer is BUY ONE GET ONE FREE on the entire drinks menu (excluding champagne), SUNDAY-FRIDAY from opening until 8pm. A clear map on the reverse with our full contact details is required please.

```html
<!DOCTYPE html>
<html lang="en">
<head>
<meta charset="utf-8">
<title>Lantern 52 – Happy Hour</title>
<link href="https://fonts.googleapis.com/css2?family=Bebas+Neue&family=Share+Tech+Mono&display=swap" rel="stylesheet">
<style>
  :root {
    --bg-deep: #1a0c24;
    --bg-violet: #4a2466;
    --bg-lilac: #8a63a8;
    --magenta: rgba(176, 28, 160, 0.82);
    --white: #ffffff;
    --gold: #b58a52;
    --map-blue: #d9eef7;
  }
  html, body {
    margin: 0;
    padding: 0;
    width: 1200px;
    height: 851px;
    overflow: hidden;
    background: var(--bg-deep);
  }
  .postcard {
    position: relative;
    width: 1200px;
    height: 851px;
    overflow: hidden;
  }
  .venue-photo {
    position: absolute;
    inset: 0;
    background:
      radial-gradient(ellipse 420px 160px at 640px 40px, #f2e9f8 0%, rgba(200,170,225,0.6) 45%, transparent 80%),
      radial-gradient(ellipse 380px 260px at 760px 300px, var(--bg-lilac) 0%, transparent 75%),
      linear-gradient(180deg, var(--bg-violet) 0%, #3a1c50 45%, var(--bg-deep) 100%);
  }
  .shapes {
    position: absolute;
    inset: 0;
  }
  .brand-name {
    position: absolute;
    top: 52px;
    left: 0;
    width: 1110px;
    text-align: center;
    font-family: "Bebas Neue", sans-serif;
    font-size: 64px;
    letter-spacing: 4px;
    color: var(--gold);
    margin: 0;
  }
  .headline {
    position: absolute;
    left: 36px;
    top: 196px;
    margin: 0;
    font-family: "Bebas Neue", sans-serif;
    font-weight: 400;
    font-size: 186px;
    line-height: 150px;
    color: var(--white);
    letter-spacing: 1px;
  }
  .offer {
    position: absolute;
    left: 36px;
    top: 498px;
    margin: 0;
    font-family: "Share Tech Mono", monospace;
    text-transform: uppercase;
    color: var(--white);
    letter-spacing: 4px;
    font-size: 23px;
    line-height: 34px;
  }
  .offer .lead { font-size: 27px; letter-spacing: 4.5px; }
  .contact {
    position: absolute;
    left: 42px;
    top: 734px;
    margin: 0;
    font-family: "Share Tech Mono", monospace;
    font-style: normal;
    font-size: 16px;
    line-height: 22px;
    letter-spacing: 2px;
    color: var(--white);
  }
  .schedule {
    position: absolute;
    left: 410px;
    top: 770px;
    margin: 0;
    font-family: "Share Tech Mono", monospace;
    text-transform: uppercase;
    font-size: 22px;
    line-height: 28px;
    letter-spacing: 3px;
    color: var(--white);
  }
</style>
</head>
<body>
<main class="postcard">
  <div class="venue-photo" role="img" aria-label="Photo of a purple-lit lounge with banquette seating, small round tables, ice buckets, wall sconces and a chandelier"></div>

  <svg class="shapes" width="1200" height="851" viewBox="0 0 1200 851" aria-hidden="false">
    <circle class="offer-disc" cx="218" cy="405" r="285" fill="var(--magenta)"/>
    <g class="map-badge" transform="translate(1058 695)">
      <g fill="var(--white)">
        <rect x="-92" y="-92" width="184" height="184"/>
        <rect x="-92" y="-92" width="184" height="184" transform="rotate(11.25)"/>
        <rect x="-92" y="-92" width="184" height="184" transform="rotate(22.5)"/>
        <rect x="-92" y="-92" width="184" height="184" transform="rotate(33.75)"/>
        <rect x="-92" y="-92" width="184" height="184" transform="rotate(45)"/>
        <rect x="-92" y="-92" width="184" height="184" transform="rotate(56.25)"/>
        <rect x="-92" y="-92" width="184" height="184" transform="rotate(67.5)"/>
        <rect x="-92" y="-92" width="184" height="184" transform="rotate(78.75)"/>
      </g>
      <circle r="108" fill="var(--map-blue)" role="img" aria-label="Street map showing the venue location near the nearby stations"/>
    </g>
  </svg>

  <p class="brand-name">Lantern 52</p>

  <h1 class="headline">Happy<br>Hour</h1>

  <p class="offer">
    <span class="lead">Buy one get one free</span><br>
    On the entire<br>
    drinks menu<br>
    (excluding champagne)
  </p>

  <address class="contact">
    52 Hollow Lane<br>
    London, United Kingdom<br>
    +44 20 7946 0321<br>
    https://social.example/lantern52
  </address>

  <p class="schedule">Sunday-Friday<br>from opening until 8pm.</p>
</main>
</body>
</html>
```